Velmora Group
Velmora Financial
Velmora Group -
Creative Brief
Pirot Brekon
Partner
318 Elmwick Lane London E9 4PQ United Kingdom
Pbrekon@quillmesh.net
Company No. 5281947
Please provide an alternative design with the name Velmora Group instead of Velmora Financial
Just the logo

```html
<!DOCTYPE html>
<html lang="en">
<head>
<meta charset="utf-8">
<title>Velmora Group – Business Card</title>
<link rel="stylesheet" href="https://fonts.googleapis.com/css2?family=Cinzel:wght@500&family=Tinos:wght@400;700&family=Arimo:wght@400&display=swap">
<style>
  :root {
    --paper-light: #ffffff;
    --paper-edge: #dcdcdc;
    --ink: #1f1f1f;
    --ink-soft: #2b2b2b;
    --accent-blue: #2f6fcf;
    --band-blue-light: #3d8ae6;
    --band-blue-dark: #0f4fb0;
    --band-rim: #8a8a8a;
    --band-text: #ffffff;
  }
  html, body {
    margin: 0;
    padding: 0;
    width: 1200px;
    height: 686px;
    overflow: hidden;
    background: var(--paper-light);
  }
  .business-card {
    position: relative;
    width: 1200px;
    height: 686px;
    overflow: hidden;
    background: radial-gradient(ellipse 70% 80% at 50% 45%, var(--paper-light) 0%, #f3f3f3 60%, var(--paper-edge) 100%);
  }
  .brand-name {
    position: absolute;
    left: 44px;
    top: 236px;
    margin: 0;
    font-family: "Cinzel", "Times New Roman", serif;
    font-weight: 500;
    font-size: 56px;
    line-height: 1;
    letter-spacing: 4px;
    text-transform: uppercase;
    color: var(--ink-soft);
    white-space: nowrap;
  }
  .license-number {
    position: absolute;
    left: 151px;
    top: 318px;
    margin: 0;
    font-family: "Arimo", Arial, sans-serif;
    font-size: 33px;
    line-height: 1.1;
    color: var(--ink);
    white-space: nowrap;
  }
  .contact-person {
    position: absolute;
    right: 38px;
    top: 192px;
    text-align: right;
  }
  .contact-person .person-name {
    margin: 0;
    font-family: "Tinos", "Times New Roman", serif;
    font-weight: 700;
    font-size: 29px;
    line-height: 1.2;
    color: var(--accent-blue);
    white-space: nowrap;
  }
  .contact-person .person-role {
    margin: 2px 0 0;
    font-family: "Arimo", Arial, sans-serif;
    font-size: 26px;
    line-height: 1.2;
    color: var(--ink);
  }
  .footer-band {
    position: absolute;
    left: 0;
    top: 0;
    width: 1200px;
    height: 686px;
  }
  .contact-details {
    position: absolute;
    right: 42px;
    top: 537px;
    margin: 0;
    text-align: right;
    font-family: "Tinos", "Times New Roman", serif;
    font-style: normal;
    font-size: 29px;
    line-height: 36px;
    color: var(--band-text);
    white-space: nowrap;
  }
</style>
</head>
<body>
  <main class="business-card">
    <h1 class="brand-name">Velmora Group</h1>
    <p class="license-number">License No. No. 5281947</p>

    <div class="contact-person">
      <p class="person-name">Pirot Brekon</p>
      <p class="person-role">Partner</p>
    </div>

    <svg class="footer-band" viewBox="0 0 1200 686" aria-hidden="true">
      <defs>
        <linearGradient id="band-fill" x1="0" y1="0" x2="0.3" y2="1">
          <stop offset="0" stop-color="var(--band-blue-light)"/>
          <stop offset="1" stop-color="var(--band-blue-dark)"/>
        </linearGradient>
      </defs>
      <path class="band-rim" d="M 348 686 C 378 414, 606 378, 1200 370 L 1200 686 Z" fill="var(--band-rim)"/>
      <path class="band-gap" d="M 360 686 C 390 422, 614 390, 1200 382 L 1200 686 Z" fill="var(--paper-light)"/>
      <path class="band-fill" d="M 370 686 C 400 430, 620 400, 1200 390 L 1200 686 Z" fill="url(#band-fill)"/>
    </svg>

    <address class="contact-details">
      318 Elmwick Lane London E9 4PQ United Kingdom<br>
      Phone : +44(0)7700900412 Cell : +44(0)7700900412<br>
      Email : Pbrekon@quillmesh.net
    </address>
  </main>
</body>
</html>
```